KVRo Business Cards

We need a business card design. We are a Technology (Audio Visual) design, sales and installation company. Looking for a double sided design, clean

Contact Information for Business Card

Clean, modern look, 2 sided

Font styles to use
Sans Serif

```html
<!DOCTYPE html>
<html lang="en">
<head>
<meta charset="utf-8">
<title>KVRo Business Cards</title>
<link href="https://fonts.googleapis.com/css2?family=Lato:wght@300;400;700;900&display=swap" rel="stylesheet">
<style>
  :root {
    --stage: #2a2d32;
    --orange: #f39320;
    --orange-deep: #ec7f1a;
    --charcoal: #3d3d3f;
    --strap: #4a4a4c;
    --white: #ffffff;
    --ink: #4b4b4d;
    --rule: #1f2a44;
  }
  * { box-sizing: border-box; margin: 0; padding: 0; }
  html, body { width: 1200px; height: 900px; overflow: hidden; }
  body {
    background: var(--stage);
    font-family: "Lato", sans-serif;
    position: relative;
  }
  .card {
    position: absolute;
    top: 300px;
    width: 520px;
    height: 300px;
    border-radius: 28px;
    overflow: hidden;
  }

  /* Front */
  .card-front {
    left: 50px;
    background: var(--white);
    border: 6px solid var(--orange);
  }
  .front-logo-block {
    position: absolute;
    left: 0; top: 70px;
    width: 178px; height: 140px;
    background: var(--charcoal);
    display: flex; align-items: center; justify-content: center;
  }
  .brand-name {
    color: var(--white);
    font-weight: 900;
    letter-spacing: 1px;
    line-height: 1;
  }
  .front-logo-block .brand-name { font-size: 52px; }
  .front-band {
    position: absolute;
    left: 178px; top: 0;
    width: 26px; height: 100%;
    background: linear-gradient(90deg, var(--orange-deep), var(--orange));
  }
  .identity {
    position: absolute;
    right: 28px; top: 30px;
    text-align: right;
    color: var(--ink);
  }
  .identity-name { font-size: 24px; font-weight: 300; }
  .identity-name strong { font-weight: 700; }
  .identity-role { font-size: 13px; margin-top: 2px; }
  .contacts {
    position: absolute;
    left: 232px; top: 110px;
    list-style: none;
  }
  .contact {
    display: flex; align-items: flex-start;
    margin-bottom: 10px;
    color: var(--ink);
    font-size: 15px;
    line-height: 1.2;
  }
  .contact-icon {
    width: 30px; height: 30px; flex: none;
    border-radius: 50%;
    background: var(--orange);
    display: flex; align-items: center; justify-content: center;
    margin-right: 12px;
  }
  .contact-text {
    border-left: 2px solid var(--rule);
    padding-left: 8px;
  }

  /* Back */
  .card-back {
    left: 630px;
    background: linear-gradient(135deg, var(--orange-deep), var(--orange));
  }
  .strap {
    position: absolute;
    top: 0; height: 100%;
    width: 22px;
    background: var(--strap);
  }
  .strap-left { left: 140px; }
  .strap-right { right: 110px; }
  .back-logo-panel {
    position: absolute;
    left: 150px; top: 95px;
    width: 240px; height: 110px;
    background: var(--charcoal);
    display: flex; align-items: center; justify-content: center;
    box-shadow: 0 3px 8px rgba(0,0,0,.25);
  }
  .back-logo-panel .brand-name { font-size: 62px; }
</style>
</head>
<body>

<section class="card card-front" aria-label="Business card front">
  <div class="front-logo-block"><span class="brand-name">KVRo</span></div>
  <div class="front-band"></div>

  <div class="identity">
    <div class="identity-name"><strong>Lorem</strong> ipsum</div>
    <div class="identity-role">Designer</div>
  </div>

  <ul class="contacts">
    <li class="contact">
      <span class="contact-icon">
        <svg width="16" height="16" viewBox="0 0 16 16" aria-hidden="true"><path d="M2 8 L8 2.5 L14 8 M4 7 V13.5 H12 V7" fill="none" stroke="#fff" stroke-width="1.8" stroke-linejoin="round"/></svg>
      </span>
      <span class="contact-text">Street Address Here<br>Italy, 2222</span>
    </li>
    <li class="contact">
      <span class="contact-icon">
        <svg width="16" height="16" viewBox="0 0 16 16" aria-hidden="true"><path d="M2 8 L14 2 L10 14 L8 9 Z" fill="#fff"/></svg>
      </span>
      <span class="contact-text">username@email.com</span>
    </li>
    <li class="contact">
      <span class="contact-icon">
        <svg width="16" height="16" viewBox="0 0 16 16" aria-hidden="true"><path d="M4 2 L6.5 2 L7.5 5 L6 6.2 C6.8 8 8 9.2 9.8 10 L11 8.5 L14 9.5 V12 C14 13 13 14 12 14 C6.5 13.6 2.4 9.5 2 4 C2 3 3 2 4 2 Z" fill="#fff"/></svg>
      </span>
      <span class="contact-text">+77 7777 7777 7777<br>+55 6767 4545 2323</span>
    </li>
    <li class="contact">
      <span class="contact-icon">
        <svg width="16" height="16" viewBox="0 0 16 16" aria-hidden="true"><g fill="none" stroke="#fff" stroke-width="1.3"><circle cx="8" cy="8" r="6"/><ellipse cx="8" cy="8" rx="2.6" ry="6"/><path d="M2 8 H14 M3 5 H13 M3 11 H13"/></g></svg>
      </span>
      <span class="contact-text">www.domainname.com</span>
    </li>
  </ul>
</section>

<section class="card card-back" aria-label="Business card back">
  <div class="strap strap-left"></div>
  <div class="strap strap-right"></div>
  <div class="back-logo-panel"><span class="brand-name">KVRo</span></div>
</section>

</body>
</html>
```